Veterinary Business cards

Redesign Business Card

Information needed on Card:
Hours: Mon-Fri: 4pm -10PM; Sat- Sun- 10 AM- 5PM
Help@bayfernvet.com
www.bayfernvet.com
555-718-2946
4173 SE 19th Ave. okc, ok 73958
*No appointment necessary*

Optional:
Our tag line is "We're here when you need us" - If it fits on the cards.

```html
<!DOCTYPE html>
<html lang="en">
<head>
<meta charset="utf-8">
<title>Bayfern Vet Urgent Care – Business Card</title>
<link href="https://fonts.googleapis.com/css2?family=Marcellus&family=Montserrat:wght@300;400&display=swap" rel="stylesheet">
<style>
  :root {
    --backdrop: #d9dde0;
    --card: #eff2f5;
    --navy: #163e68;
    --orange: #d47b2c;
    --ink: #262626;
  }
  * { margin: 0; padding: 0; box-sizing: border-box; }
  html, body { width: 1200px; height: 1200px; overflow: hidden; }
  body { background: var(--backdrop); position: relative; font-family: "Montserrat", sans-serif; }

  .card {
    position: absolute;
    left: 178px;
    width: 821px;
    height: 493px;
    background: var(--card);
  }
  .card--front { top: 91px; }
  .card--back { top: 595px; }

  .brand {
    position: absolute;
    left: 0; right: 0;
    text-align: center;
    font-family: "Marcellus", serif;
    font-weight: 400;
    color: var(--navy);
    line-height: 1;
  }
  .brand__name { display: block; letter-spacing: 0.04em; }
  .brand__sub { display: block; letter-spacing: 0.14em; }

  .card--front .brand { top: 192px; }
  .card--front .brand__name { font-size: 62px; }
  .card--front .brand__sub { font-size: 25px; margin-top: 12px; }

  .card--back .brand { top: 90px; }
  .card--back .brand__name { font-size: 48px; }
  .card--back .brand__sub { font-size: 19px; margin-top: 8px; }

  .tagline {
    position: absolute;
    top: 168px; left: 0; right: 0;
    text-align: center;
    color: var(--orange);
    font-weight: 300;
    font-size: 22px;
    letter-spacing: -0.01em;
  }

  .contact-list {
    position: absolute;
    top: 209px;
    left: 93px;
    list-style: none;
  }
  .contact-list__item {
    display: flex;
    align-items: center;
    height: 35px;
    margin-bottom: 5px;
    color: var(--ink);
    font-size: 20px;
    font-weight: 300;
    letter-spacing: 0.02em;
  }
  .contact-list__icon {
    width: 35px; height: 35px;
    flex: none;
    margin-right: 12px;
  }
</style>
</head>
<body>

  <section class="card card--front">
    <div class="brand">
      <span class="brand__name">BAYFERN VET</span>
      <span class="brand__sub">URGENT CARE</span>
    </div>
  </section>

  <section class="card card--back">
    <div class="brand">
      <span class="brand__name">BAYFERN VET</span>
      <span class="brand__sub">URGENT CARE</span>
    </div>
    <p class="tagline">No Appointment Necessary</p>

    <ul class="contact-list">
      <li class="contact-list__item">
        <svg class="contact-list__icon" viewBox="0 0 36 36" aria-hidden="true">
          <circle cx="18" cy="18" r="18" fill="#d47b2c"/>
          <circle cx="18" cy="18" r="10" fill="none" stroke="#fff" stroke-width="1.6"/>
          <path d="M18 12v6l3.5 3" fill="none" stroke="#fff" stroke-width="1.6" stroke-linecap="round"/>
        </svg>
        Mon-Fri: 4pm -10PM; Sat- Sun- 10 AM- 5PM
      </li>
      <li class="contact-list__item">
        <svg class="contact-list__icon" viewBox="0 0 36 36" aria-hidden="true">
          <circle cx="18" cy="18" r="18" fill="#d47b2c"/>
          <path d="M18 29s-8-8.5-8-14a8 8 0 0 1 16 0c0 5.5-8 14-8 14z" fill="none" stroke="#fff" stroke-width="1.6" stroke-linejoin="round"/>
          <circle cx="18" cy="15" r="3" fill="none" stroke="#fff" stroke-width="1.6"/>
        </svg>
        4173 SE 19th Ave. okc, ok 73958
      </li>
      <li class="contact-list__item">
        <svg class="contact-list__icon" viewBox="0 0 36 36" aria-hidden="true">
          <circle cx="18" cy="18" r="18" fill="#d47b2c"/>
          <g fill="none" stroke="#fff" stroke-width="1.5">
            <circle cx="18" cy="18" r="11"/>
            <ellipse cx="18" cy="18" rx="5" ry="11"/>
            <path d="M7 18h22M9 12h18M9 24h18"/>
          </g>
        </svg>
        www.bayfernvet.com
      </li>
      <li class="contact-list__item">
        <svg class="contact-list__icon" viewBox="0 0 36 36" aria-hidden="true">
          <circle cx="18" cy="18" r="18" fill="#d47b2c"/>
          <g fill="none" stroke="#fff" stroke-width="1.6" stroke-linejoin="round">
            <rect x="8" y="11" width="20" height="14" rx="1.5"/>
            <path d="M8 12l10 8 10-8"/>
          </g>
        </svg>
        Help@bayfernvet.com
      </li>
      <li class="contact-list__item">
        <svg class="contact-list__icon" viewBox="0 0 36 36" aria-hidden="true">
          <circle cx="18" cy="18" r="18" fill="#d47b2c"/>
          <path d="M11 9c-1.5 1-2 2.5-1 5 2 5 6 9.5 11 12 2.5 1 4 .5 5-1l.5-1.2-4-2.8-2 1.5c-2.5-1.2-5-3.8-6.2-6.3l1.5-2-2.8-4z" fill="none" stroke="#fff" stroke-width="1.5" stroke-linejoin="round"/>
        </svg>
        555-718-2946
      </li>
    </ul>
  </section>

</body>
</html>
```